" a empresa trabalha na area de divulgação, e marketing usando a ferramenta instagram e facebook, usando o perfil de seus clientes, transformando em e-commerce, é tambem atua na area de vendas de paineis de led em acrilico "

```html
<!DOCTYPE html>
<html lang="pt-BR">
<head>
<meta charset="UTF-8">
<title>Vitrine – Cartão de visita</title>
<link rel="stylesheet" href="https://fonts.googleapis.com/css2?family=Montserrat:wght@400;500;600&display=swap">
<style>
  :root {
    --page: #e9eaee;
    --card-light: #f7f5f8;
    --card-pink: #c8347a;
    --card-magenta: #a0185a;
    --card-violet: #6a2a74;
    --accent: #d83a7c;
    --accent-soft: #f08ab2;
    --ink: #2b2630;
    --logo-box: #3a1f2e;
    --logo-text: #ffffff;
    --figure-warm: #e8a23c;
    --figure-cool: #4a3a52;
  }
  * { box-sizing: border-box; margin: 0; padding: 0; }
  html, body { width: 1200px; height: 1200px; overflow: hidden; }
  body {
    background: var(--page);
    font-family: "Montserrat", sans-serif;
    color: var(--ink);
    position: relative;
  }
  .business-card {
    position: absolute;
    left: 80px;
    top: 303px;
    width: 1040px;
    height: 594px;
    border-radius: 26px;
    overflow: hidden;
    background: linear-gradient(100deg,
      var(--card-light) 0%, var(--card-light) 38%,
      #f1d3e2 52%, var(--card-pink) 70%, var(--card-magenta) 86%, var(--card-violet) 100%);
    box-shadow: 0 20px 50px rgba(60, 20, 50, .18);
    border-bottom: 6px solid var(--accent);
  }
  .name-band {
    position: absolute;
    left: 0; top: 70px;
    width: 520px; height: 84px;
    background: linear-gradient(90deg, var(--accent) 0%, var(--accent-soft) 22%, rgba(255,255,255,0) 60%);
  }
  .avatar-badge {
    position: absolute;
    left: 58px; top: 78px;
    width: 68px; height: 68px;
    border-radius: 50%;
    background: var(--accent);
    border: 4px solid #fff;
  }
  .avatar-badge svg { width: 100%; height: 100%; }
  .holder-name {
    position: absolute;
    left: 152px; top: 80px;
    font-size: 31px; font-weight: 600;
    letter-spacing: .5px;
    text-transform: uppercase;
  }
  .holder-role {
    position: absolute;
    left: 152px; top: 120px;
    font-size: 24px; font-weight: 400;
    letter-spacing: 1px;
    text-transform: uppercase;
  }
  .contact-list { list-style: none; position: absolute; left: 55px; top: 262px; }
  .contact-item {
    display: flex; align-items: center;
    height: 40px; margin-bottom: 17px;
    font-size: 28px; font-weight: 500;
  }
  .contact-icon {
    width: 40px; height: 40px;
    border-radius: 8px;
    background: var(--accent);
    margin-right: 27px;
    flex-shrink: 0;
  }
  .contact-icon svg { width: 100%; height: 100%; }
  .brand-box {
    position: absolute;
    left: 602px; top: 48px;
    width: 362px; height: 132px;
    border-radius: 14px;
    background: var(--logo-box);
    display: flex; align-items: center; justify-content: center;
    gap: 20px;
  }
  .brand-mark { width: 26px; height: 26px; background: var(--logo-text); }
  .brand-name {
    color: var(--logo-text);
    font-size: 44px; font-weight: 500;
    letter-spacing: 2px;
  }
  .mascot-area {
    position: absolute;
    left: 628px; top: 182px;
    width: 312px; height: 406px;
    border-radius: 20px 20px 0 0;
    background: linear-gradient(180deg, var(--figure-warm) 0%, #c96a3a 45%, var(--figure-cool) 100%);
    opacity: .85;
  }
</style>
</head>
<body>
  <article class="business-card">
    <div class="name-band"></div>
    <div class="avatar-badge">
      <svg viewBox="0 0 60 60"><circle cx="30" cy="23" r="9" fill="#fff"/><path d="M14 46c2-10 9-14 16-14s14 4 16 14z" fill="#fff"/></svg>
    </div>
    <h1 class="holder-name">Rafael Moreira</h1>
    <p class="holder-role">General Manager</p>

    <ul class="contact-list">
      <li class="contact-item">
        <span class="contact-icon"><svg viewBox="0 0 40 40"><path d="M13 10l5 5-3 3c1 3 4 6 7 7l3-3 5 5-3 3c-8 0-17-9-17-17z" fill="#fff"/></svg></span>
        (44) 9555-0147
      </li>
      <li class="contact-item">
        <span class="contact-icon"><svg viewBox="0 0 40 40"><rect x="9" y="12" width="22" height="16" rx="2" fill="#fff"/><path d="M9 13l11 8 11-8" stroke="#d83a7c" stroke-width="2" fill="none"/></svg></span>
        rafael@vitrinecom.com.br
      </li>
      <li class="contact-item">
        <span class="contact-icon"><svg viewBox="0 0 40 40"><path d="M13 11l14 8-6 2-2 7z" fill="#fff"/></svg></span>
        www.vitrinecom.com.br
      </li>
      <li class="contact-item">
        <span class="contact-icon"><svg viewBox="0 0 40 40"><circle cx="20" cy="20" r="7" fill="#fff"/></svg></span>
        @vitrinecombr
      </li>
    </ul>

    <div class="brand-box">
      <span class="brand-mark"></span>
      <span class="brand-name">VITRINE</span>
    </div>

    <div class="mascot-area" role="img" aria-label="Mascote ilustrado da marca segurando o logotipo acima da cabeça"></div>
  </article>
</body>
</html>
```